Harbor Quill Note Card Stationary

We need a Note Card with envelope using the attached photo. I would like for photo
a. to bleed to the edges, no border or white space.
b. to have a weathered look if possible
c. to have two styles, folded and single.
d. to reflect the color of the photo as much as possible.
e. to provide following return address on envelope
Harbor Quill 57 Wexmore Ln. Jamaica Plain MA 02187

Target Market(s)

Mailing List

Industry/Entity Type

Religious

Font styles to use
Other font styles liked:
• no preference

Requirements
Must have
• Varied sizes
Nice to have
• Weathers look
Should not have
• blurred finish, color distortion

```html
<!DOCTYPE html>
<html lang="en">
<head>
<meta charset="utf-8">
<title>Harbor Quill Note Card Stationery</title>
<link rel="stylesheet" href="https://fonts.googleapis.com/css2?family=Cabin:wght@400;500&display=swap">
<style>
  :root {
    --backdrop: #f1f1f0;
    --card-brown: #6f5d45;
    --card-brown-light: #8a775d;
    --sky-top: #3a3128;
    --sky-mid: #7d6a52;
    --night: #1d1914;
    --city-glow: #b08a55;
    --water: #262219;
    --ink-light: #efe7da;
    --envelope: #725f46;
    --envelope-line: #5f4e39;
    --seal: #8f7c63;
  }
  * { box-sizing: border-box; margin: 0; padding: 0; }
  html, body { width: 1200px; height: 800px; overflow: hidden; }
  body {
    background: var(--backdrop);
    font-family: "Cabin", sans-serif;
    position: relative;
  }
  .piece {
    position: absolute;
    width: 500px;
    height: 340px;
    box-shadow: 0 6px 18px rgba(0,0,0,0.18);
    overflow: hidden;
  }
  .front-a { left: 70px;  top: 40px; }
  .front-b { left: 630px; top: 40px; }
  .back    { left: 70px;  top: 420px; }
  .envelope{ left: 630px; top: 420px; }

  .card-front { background: var(--night); }
  .skyline-photo {
    position: absolute; inset: 0;
    background:
      radial-gradient(ellipse 60% 30% at 30% 20%, rgba(160,140,112,0.55), transparent 70%),
      radial-gradient(ellipse 50% 25% at 75% 35%, rgba(130,112,88,0.45), transparent 70%),
      linear-gradient(180deg, var(--sky-mid) 0%, var(--sky-top) 35%, var(--night) 52%,
        var(--city-glow) 58%, #4a3b2a 66%, var(--water) 72%, #14120e 100%);
  }
  .front-title {
    position: absolute; top: 34px; left: 0; right: 0;
    text-align: center;
    color: var(--ink-light);
    font-size: 27px; font-weight: 400; line-height: 1.25;
    letter-spacing: 0.5px;
    opacity: 0.9;
  }
  .front-verse {
    position: absolute; bottom: 44px; left: 30px; right: 30px;
    text-align: center;
    color: var(--ink-light);
    font-size: 10.5px; line-height: 1.45;
  }

  .card-back {
    background:
      radial-gradient(ellipse 35% 18% at 45% 10%, var(--card-brown-light), transparent 75%),
      radial-gradient(ellipse 30% 15% at 28% 30%, rgba(138,119,93,0.7), transparent 75%),
      radial-gradient(ellipse 25% 12% at 65% 22%, rgba(138,119,93,0.6), transparent 75%),
      var(--card-brown);
  }
  .return-address {
    position: absolute; left: 22px; bottom: 20px;
    color: var(--ink-light);
    font-size: 16px; letter-spacing: 0.3px;
  }

  .envelope-back { background: var(--envelope); }
  .envelope-back svg { position: absolute; inset: 0; }
</style>
</head>
<body>
  <section class="piece card-front front-a">
    <div class="skyline-photo" role="img" aria-label="Night photograph of the Boston skyline lit across the harbor under clouded sky"></div>
    <h1 class="front-title">In Boston As It Is In Heaven<br>2017</h1>
    <p class="front-verse">In all my prayers for all of you, I always pray with joy because of your partnership in the gospel<br>from the first day until now... Philippians 1:4-5</p>
  </section>

  <section class="piece card-front front-b">
    <div class="skyline-photo" role="img" aria-label="Night photograph of the Boston skyline lit across the harbor under clouded sky"></div>
    <h1 class="front-title">In Boston As It Is In Heaven<br>2017</h1>
    <p class="front-verse">In all my prayers for all of you, I always pray with joy because of your partnership in the gospel<br>from the first day until now... Philippians 1:4-5</p>
  </section>

  <section class="piece card-back back" role="img" aria-label="Card back with faint weathered cloud texture">
    <p class="return-address">Harbor Quill 57 Wexmore Ln. Jamaica Plain MA 02187</p>
  </section>

  <section class="piece envelope-back envelope">
    <svg width="500" height="340" viewBox="0 0 500 340">
      <polyline points="0,0 250,200 500,0" fill="rgba(0,0,0,0.05)" stroke="var(--envelope-line)" stroke-width="1.2"/>
      <line x1="0" y1="340" x2="210" y2="170" stroke="var(--envelope-line)" stroke-width="1"/>
      <line x1="500" y1="340" x2="290" y2="170" stroke="var(--envelope-line)" stroke-width="1"/>
      <circle cx="250" cy="196" r="16" fill="var(--seal)"/>
    </svg>
  </section>
</body>
</html>
```